Creative Web Design - Intl Market Research Company

We need an innovative web design for an emerging company into the international market research marketplace.

The company, Halvenor Associates, is a Trade, Investment, and Market Research company. Halvenor offers domestic and international companies increased success in the U.S. marketplace by providing a variety of services. (seen on attached brochure)

The website should be cutting edge and creative while having an easy navigation. The color is not fixed and attached logo is not finalized, feel free to post anything from conservative to progressive options. Keep in mind target customers are domestic and international businesses looking to emerge/improve in the U.S. marketplace.

Additional Company information is located in the attached documentation. The documentation is outdated & winner will have priority standing for our next projects.(logo & document re-design)

I have received a few e-mail requests and have updated the status to guaranteed payment.

Thanks!

Target Market(s)

Any company, foreign and domestic, looking to introduce their product into the U.S. marketplace.

Industry/Entity Type

Market Research

Requirements
Must have
• Easy Navigation
Should not have
• Too many buttons
Difficult navigation
Excessive Typography

```html
<!DOCTYPE html>
<html lang="en">
<head>
<meta charset="utf-8">
<title>Halvenor Associates</title>
<link href="https://fonts.googleapis.com/css2?family=Mulish:wght@300;400;600;700&display=swap" rel="stylesheet">
<style>
:root{
  --page:#fbf7e9;
  --panel:#ffffff;
  --border:#e9e0b8;
  --gold-top:#b3a45c;
  --gold-bottom:#958640;
  --gold:#a2934a;
  --ink:#333333;
  --muted:#8c8c8c;
  --soft:#b0b0b0;
  --link:#3a8fd0;
  --dot:#d2d2d2;
}
*{margin:0;padding:0;box-sizing:border-box}
html,body{width:1041px;height:1200px;overflow:hidden}
body{background:var(--page);font-family:"Mulish",Arial,sans-serif;color:var(--ink);position:relative}
.abs{position:absolute}
.top-links{left:780px;top:11px;width:138px;text-align:right;font-size:10px;font-weight:600;color:#333}
.brand{left:113px;top:30px;display:flex;align-items:center;gap:10px}
.brand-mark{width:44px;height:44px;border-radius:50%;background:var(--gold)}
.brand-name{font-size:22px;font-weight:700;color:#222;letter-spacing:.2px}
.support{left:751px;top:56px;display:flex;align-items:center;gap:8px}
.support-text small{display:block;font-size:9.5px;color:#333}
.support-text strong{display:block;font-size:19px;font-weight:400;color:#222;line-height:1.05}
.nav{left:95px;top:104px;width:850px;height:39px;border-radius:3px;background:linear-gradient(var(--gold-top),var(--gold-bottom));border:1px solid #8d7f3c}
.nav a{position:absolute;top:11px;font-size:12.5px;font-weight:700;color:#fff;text-decoration:none;transform:translateX(-50%)}
.nav .home{left:7px;top:6px;width:70px;height:26px;background:#fff;border-radius:3px;color:#555;font-weight:600;text-align:center;line-height:26px;transform:none}
.search{position:absolute;left:630px;top:6px;width:204px;height:26px;background:#fff;border-radius:3px;font-size:10px;color:#aaa;padding:7px 14px}
.search svg{position:absolute;right:9px;top:5px}
.main{left:95px;top:152px;width:850px;height:737px;background:var(--panel);border:1px solid var(--border);border-radius:3px}
.hero-photo{left:96px;top:153px;width:848px;height:340px;background:linear-gradient(90deg,#c7b6a5 0%,#9b8d84 18%,#d7d2cc 38%,#ece9e6 52%,#ffffff 64%)}
.hero-line{left:96px;top:493px;width:848px;height:1px;background:var(--border)}
.hero-title{left:560px;top:216px;width:370px;text-align:center;font-size:22.5px;font-weight:300;line-height:31px;color:#222}
.hero-sub{left:575px;top:322px;width:340px;text-align:center;font-size:12px;line-height:20px;color:#666}
.read-more{left:673px;top:382px;width:150px;height:49px;border-radius:25px;background:linear-gradient(#b6a862,#958640);box-shadow:0 3px 3px rgba(0,0,0,.2);color:#fff;font-size:14px;font-weight:600}
.read-more span{position:absolute;left:50px;top:16px}
.read-more i{position:absolute;left:38px;top:0;width:1px;height:49px;background:rgba(255,255,255,.35)}
.read-more svg{position:absolute;left:16px;top:19px}
.dots{left:838px;top:466px;display:flex;gap:8px}
.dots b{width:9px;height:9px;background:var(--dot)}
.dots b:first-child{background:var(--gold)}
.feature-icon{top:534px}
.feature h3{font-size:16px;font-weight:400;color:#333;margin-left:0}
.feature{top:537px;width:219px}
.feature .lead{font-size:11px;color:var(--soft);margin-top:5px;padding-bottom:7px;border-bottom:1px solid #ececec;letter-spacing:.3px}
.feature p{font-size:10.5px;line-height:17.5px;color:var(--muted);margin-top:10px;letter-spacing:.2px}
.welcome h2{font-size:21px;font-weight:400;color:#333}
.welcome{left:120px;top:680px;width:576px}
.welcome p{font-size:10.5px;line-height:19px;color:var(--muted);margin-top:4px}
.welcome p.first{margin-top:20px}
.welcome-photo{left:713px;top:725px;width:207px;height:127px;border-radius:3px;background:linear-gradient(135deg,#c9b394,#7f9cbf 55%,#d6cfc5)}
.info{left:95px;top:902px;width:850px;height:213px;background:var(--panel);border:1px solid var(--border);border-radius:3px}
.col h3{font-size:16px;font-weight:400;color:#333}
.col{top:925px}
.about{left:120px;width:278px}
.about p{font-size:10.5px;line-height:19px;color:var(--muted);margin-top:13px}
.stay{left:432px;width:220px}
.stay p{font-size:10px;line-height:15.6px;color:var(--muted);margin-top:10px;padding-left:2px}
.email{position:absolute;left:1px;top:93px;width:199px;height:23px;border:1px solid #cfcfcf;border-radius:3px;font-size:10px;color:#b5b5b5;padding:4px 11px;background:linear-gradient(#f5f5f5,#fff)}
.signup{position:absolute;left:-2px;top:133px;width:200px;height:26px;border-radius:3px;background:linear-gradient(#4a4a4a,#222);color:#fff;font-size:9.5px;font-weight:600;letter-spacing:.5px;text-align:center;line-height:26px}
.blog{left:699px;width:220px}
.blog ul{list-style:none;margin-top:12px}
.blog li{position:relative;font-size:10px;line-height:12.5px;color:var(--link);margin-bottom:9px;letter-spacing:.3px}
.blog li::before{content:"";position:absolute;left:-14px;top:3px;width:5px;height:5px;background:#777;transform:rotate(45deg)}
.footer{left:95px;top:1135px;width:850px;height:40px;border-radius:3px;background:linear-gradient(var(--gold-top),var(--gold-bottom));border:1px solid #8d7f3c;color:#fff;font-size:11.5px}
.footer .copy{position:absolute;left:24px;top:13px}
.footer nav{position:absolute;right:24px;top:13px;display:flex;gap:19px}
</style>
</head>
<body>
<div class="abs top-links">Enquiry | SiteMap</div>

<div class="abs brand">
  <div class="brand-mark"></div>
  <div class="brand-name">Halvenor Associates</div>
</div>

<div class="abs support">
  <svg width="34" height="34" viewBox="0 0 34 34" aria-hidden="true">
    <path d="M5 19 V15 A12 12 0 0 1 29 15 V19" fill="none" stroke="#333" stroke-width="2.5"/>
    <rect x="2" y="16" width="7" height="11" rx="3" fill="#333"/>
    <rect x="25" y="16" width="7" height="11" rx="3" fill="#333"/>
    <path d="M28 27 Q26 32 18 32" fill="none" stroke="#333" stroke-width="1.5"/>
    <circle cx="17" cy="32" r="1.8" fill="#333"/>
  </svg>
  <div class="support-text"><small>24/7 Online Support Service</small><strong>1-800-555-0142</strong></div>
</div>

<nav class="abs nav">
  <a class="home" href="#">Home</a>
  <a href="#" style="left:119px">Services</a>
  <a href="#" style="left:208px">Industries</a>
  <a href="#" style="left:295px">Benefits</a>
  <a href="#" style="left:382px">About Us</a>
  <a href="#" style="left:475px">Resources</a>
  <a href="#" style="left:573px">Contact Us</a>
  <div class="search">Search
    <svg width="15" height="15" viewBox="0 0 15 15" aria-hidden="true"><circle cx="9" cy="6" r="4.5" fill="none" stroke="#aaa" stroke-width="1.2"/><path d="M5.8 9.2 L1.5 13.5" stroke="#aaa" stroke-width="1.4"/></svg>
  </div>
</nav>

<div class="abs main"></div>
<div class="abs hero-photo" role="img" aria-label="Photo of a smiling businesswoman in front of colleagues in a meeting"></div>
<div class="abs hero-line"></div>
<div class="abs hero-title">Dolore eu feugiat nulla facilisis at vero eros et accumsan&nbsp; odio dignissim qui blandit praesent</div>
<div class="abs hero-sub">Lorem ipsum dolor sit amet, consectetuer adipiscing elit, sed diam nonummy nibh euismod tincidunt.</div>
<div class="abs read-more">
  <svg width="9" height="10" viewBox="0 0 9 10" aria-hidden="true"><path d="M0 0 L9 5 L0 10Z" fill="#fff"/></svg>
  <i></i><span>READ MORE</span>
</div>
<div class="abs dots"><b></b><b></b><b></b><b></b></div>

<svg class="abs feature-icon" style="left:119px" width="30" height="26" viewBox="0 0 30 26" aria-hidden="true"><rect x="1.5" y="4.5" width="20" height="20" fill="none" stroke="#9c8d45" stroke-width="2.5"/><path d="M6 12 L12 19 L28 1" fill="none" stroke="#9c8d45" stroke-width="3.5"/></svg>
<div class="abs feature" style="left:160px"><h3>Trading</h3><div class="lead">Lorem Ipsum est simplement du</div><p>Dolore eu feugiat nulla facilisis at vero eros et accumsan et iusto odio dignissim qui blandit praesent luptatum zzril delenit.</p></div>

<svg class="abs feature-icon" style="left:389px" width="30" height="26" viewBox="0 0 30 26" aria-hidden="true"><rect x="1.5" y="4.5" width="20" height="20" fill="none" stroke="#9c8d45" stroke-width="2.5"/><path d="M6 12 L12 19 L28 1" fill="none" stroke="#9c8d45" stroke-width="3.5"/></svg>
<div class="abs feature" style="left:433px"><h3>Investment</h3><div class="lead">Lorem Ipsum est simplement du</div><p>Dolore eu feugiat nulla facilisis at vero eros et accumsan et iusto odio dignissim qui blandit praesent luptatum zzril delenit.</p></div>

<svg class="abs feature-icon" style="left:657px" width="30" height="26" viewBox="0 0 30 26" aria-hidden="true"><rect x="1.5" y="4.5" width="20" height="20" fill="none" stroke="#9c8d45" stroke-width="2.5"/><path d="M6 12 L12 19 L28 1" fill="none" stroke="#9c8d45" stroke-width="3.5"/></svg>
<div class="abs feature" style="left:698px"><h3>Market Research</h3><div class="lead">Lorem Ipsum est simplement du</div><p>Dolore eu feugiat nulla facilisis at vero eros et accumsan et iusto odio dignissim qui blandit praesent luptatum zzril delenit.</p></div>

<div class="abs welcome">
  <h2>Welcome to Halvenor Associates</h2>
  <p class="first">Lorem Ipsum est simplement du faux texte employé dans la sition et la misen page avant impression. Le Lorem Ipsum est le faux texte standard de l'imprimerie depuis les années 1500, quand un peintre anonyme assembla ensemble des morceaux de texte pour réaliser un livre spécimen de polices de texte. Il n'a pas fait que survivre cinq siècles, mais s'est aussi adapté à la bureautique informatique, sans que son contenu n'en soit modifié.</p>
  <p>Popularisé dans les années 1960 grâce à la vente de feuilles Transfera contenant des passages du Lorem Ipsum, et, plus récemment, par son inclusion dans des applications de mise en page de texte, comme Folio Layout.Lorem Ipsum est simplement du faux texte employé dans la sition et la misen page avant impression.</p>
</div>
<div class="abs welcome-photo" role="img" aria-label="Photo of business partners shaking hands at a meeting table"></div>

<div class="abs info"></div>
<div class="abs col about"><h3>About Us</h3><p>Lorem Ipsum est simplement faux texte employé dans la sition et la misen page avant impression. Le Lorem Ipsum est le faux texte standard imprimerie depuis&nbsp; les années 1500, quand un peintre anonyme assembla ensemble des morceaux de texte pour réaliser un livre spécimen de polices de texte. Il n'a pas fait que survivre cinq siècles, mais s'est aussi adapté.</p></div>
<div class="abs col stay"><h3>Stay Informed</h3><p>Receive critical news and research on Enterprise mobility, delivered weekly to your inbox.</p>
  <div class="email">Your Email</div>
  <div class="signup">SIGN UP FOR NEWSLETTER</div>
</div>
<div class="abs col blog"><h3>Recent Blog Post</h3>
  <ul>
    <li>Hispanic Heritage Month at CallBridge!</li>
    <li>10 Tips for Time Management: Appoint-ment Setting</li>
    <li>Multi-Cultural Customer Service at CallBridge</li>
    <li>August 2012- Team Member Spotlight: Mirela T.</li>
    <li>Translation Ethics</li>
  </ul>
</div>

<footer class="abs footer">
  <span class="copy">© Company Name. All rights reserved.</span>
  <nav><span>Home</span><span>About Us</span><span>Services</span><span>News &amp; Comments</span><span>Contact Us</span></nav>
</footer>
</body>
</html>
```